JesterVolt Balloon Logo and Product Packaging Design

I need a package design for twisting balloons for my website jestervoltfun.com. The brand name that we will use is "jestervolt". The packaging will be 40cm long x 15 cm width with a see thru front and a top that can tear off. We can only use 3 colors max, but two colors would be better. We also will need a logo for "jestervolt". I have included our mockup front and back, our competitors packaging and our style guide. You can use our style guide and our mockups for inspiration but you please don't follow it exactly. You can also ignore them all together. Thanks, Corin

```html
<!DOCTYPE html>
<html lang="en">
<head>
<meta charset="utf-8">
<title>JesterVolt Twisty Balloons Packaging</title>
<link rel="stylesheet" href="https://fonts.googleapis.com/css2?family=Amatic+SC:wght@700&family=Fredoka:wght@600&family=Oswald:wght@500;600&display=swap">
<style>
  :root {
    --red: #ff1d25;
    --ink: #1a1a1a;
    --white: #ffffff;
    --paper: #ffffff;
    --art: #ffe3e4;
  }
  * { margin: 0; padding: 0; box-sizing: border-box; }
  html, body { width: 1043px; height: 1200px; overflow: hidden; background: var(--paper); }
  .canvas { position: relative; width: 1043px; height: 1200px; }

  .card {
    position: absolute; top: 140px; width: 345px; height: 919px;
    background: var(--white);
    box-shadow: 0 1px 6px rgba(0,0,0,0.18);
    overflow: hidden;
  }
  .card--front { left: 151px; }
  .card--back { left: 565px; }
  .card__header { position: absolute; left: 0; top: 0; width: 345px; height: 170px; }

  .brand-name {
    position: absolute; left: 0; width: 100%; text-align: center;
    font-family: "Fredoka", sans-serif; font-weight: 600; font-size: 54px; line-height: 1; letter-spacing: 0.5px;
  }
  .tagline {
    position: absolute; left: 0; width: 100%; text-align: center;
    font-family: "Fredoka", sans-serif; font-weight: 600; color: var(--red);
  }

  /* front */
  .pcs-badge {
    position: absolute; left: 11px; top: 33px; width: 82px; height: 82px;
    border: 4px solid var(--white); border-radius: 50%;
    color: var(--white); font-family: "Fredoka", sans-serif; font-weight: 600; font-size: 24px; line-height: 0.95;
    display: flex; align-items: center; justify-content: center; text-align: center;
    transform: rotate(-8deg);
  }
  .headline {
    position: absolute; left: 100px; top: 40px;
    color: var(--white); font-family: "Oswald", sans-serif; font-weight: 600;
    font-size: 30px; line-height: 1.12; letter-spacing: 1px; transform: rotate(-4deg);
    transform-origin: left top;
  }
  .age-badge {
    position: absolute; left: 305px; top: 12px; width: 28px; height: 38px;
    background: var(--white); border-radius: 3px; color: var(--red);
    font-family: "Oswald", sans-serif; text-align: center; line-height: 1;
  }
  .age-badge small { display: block; font-size: 8px; margin-top: 3px; }
  .age-badge strong { display: block; font-size: 20px; font-weight: 600; }
  .balloon-art { position: absolute; background: var(--art); border-radius: 18px; }
  .balloon-art--butterfly { left: 216px; top: 30px; width: 44px; height: 38px; }
  .balloon-art--dog { left: 268px; top: 50px; width: 64px; height: 56px; }
  .card--front .brand-name { top: 145px; color: var(--red); }
  .card--front .tagline { top: 205px; font-size: 21px; transform: rotate(-2deg); }

  .warning {
    position: absolute; left: 125px; top: 804px; width: 200px; height: 94px;
    border: 2px solid var(--red); border-radius: 6px; padding: 6px 8px;
    font-family: "Oswald", sans-serif; color: var(--ink);
  }
  .warning__title { font-size: 13px; font-weight: 500; letter-spacing: 0.5px; white-space: nowrap; }
  .warning__body { margin-top: 2px; font-size: 7.6px; line-height: 11.4px; text-align: justify; letter-spacing: 0.3px; }

  /* back */
  .card--back .brand-name { top: 45px; color: var(--white); }
  .card--back .tagline { top: 143px; font-size: 31px; line-height: 38px; }
  .copy {
    position: absolute; left: 30px; top: 240px; width: 285px; text-align: center;
    font-family: "Amatic SC", sans-serif; font-weight: 700; color: var(--ink);
    font-size: 19px; line-height: 20px; letter-spacing: 0.2px;
  }
  .copy p + p { margin-top: 20px; }
  .site {
    position: absolute; top: 660px; left: 0; width: 100%; text-align: center;
    font-family: "Oswald", sans-serif; font-weight: 500; font-size: 14px; letter-spacing: 1px; color: var(--ink);
  }
  .shop-name {
    position: absolute; top: 694px; left: 0; width: 100%; text-align: center;
    font-family: "Fredoka", sans-serif; font-weight: 600; font-size: 32px; line-height: 34px; color: var(--red);
  }
  .shop-slogan {
    position: absolute; top: 768px; left: 0; width: 100%; text-align: center;
    font-family: "Oswald", sans-serif; font-weight: 500; font-size: 12.5px; letter-spacing: 0.8px; color: var(--ink);
  }
  .shop-city {
    position: absolute; top: 788px; left: 0; width: 100%; text-align: center;
    font-family: "Oswald", sans-serif; font-weight: 500; font-size: 11px; letter-spacing: 1px; font-style: italic; color: var(--ink);
  }
  .marks { position: absolute; left: 24px; top: 829px; display: flex; gap: 14px; }
  .mark { width: 26px; height: 26px; }
  .specs {
    position: absolute; left: 208px; top: 838px; width: 124px;
    font-family: "Oswald", sans-serif; color: var(--ink); line-height: 1.1; white-space: nowrap;
  }
  .specs__big { font-size: 17px; letter-spacing: 0.5px; }
  .specs__mid { font-size: 10px; font-weight: 500; letter-spacing: 0.4px; }
  .specs__small { font-size: 5.6px; letter-spacing: 0.3px; margin-top: 2px; }
  .specs__foot { font-size: 8.6px; margin-top: 7px; letter-spacing: 0.3px; word-spacing: 2px; }
</style>
</head>
<body>
<div class="canvas">

  <section class="card card--front">
    <svg class="card__header" viewBox="0 0 345 170" aria-hidden="true">
      <path d="M0 0 H345 V155 C300 120 230 125 178 131 C110 138 50 128 0 114 Z" fill="var(--red)"/>
      <path d="M197 124 C250 118 305 128 335 158 C300 138 250 130 197 124 Z" fill="var(--white)"/>
      <rect x="137" y="22" width="52" height="9" rx="4.5" fill="var(--white)"/>
      <circle cx="163" cy="22" r="5" fill="var(--white)"/>
    </svg>
    <div class="pcs-badge">100<br>PCS</div>
    <div class="headline">TWISTY<br>BALLOONS!</div>
    <div class="balloon-art balloon-art--butterfly" role="img" aria-label="Illustration of a balloon butterfly"></div>
    <div class="balloon-art balloon-art--dog" role="img" aria-label="Illustration of a balloon dog"></div>
    <div class="age-badge"><small>AGES</small><strong>8+</strong></div>
    <div class="brand-name">JesterVolt</div>
    <div class="tagline">High-Quality Party Balloons</div>

    <div class="warning">
      <div class="warning__title">&#9888; WARNING: CHOKING HAZARD</div>
      <p class="warning__body">CHILDERN UNDER EIGHT (8) YEARS OLD CAN CHOKE OR SUFFOCATE ON UNINFLATED OR BROKEN BALLOONS. ADULT SUPERVISION IS REQUIRED. KEEP UNIFLATED BALLOONS FROM REACH OF CHILDEN. DISCARD BROKEN BALLOONS RESPONSIBLY.</p>
    </div>
  </section>

  <section class="card card--back">
    <svg class="card__header" viewBox="0 0 345 170" aria-hidden="true">
      <path d="M0 0 H345 V102 C300 125 230 135 170 131 C110 127 40 130 0 155 Z" fill="var(--red)"/>
      <path d="M12 160 C40 132 100 118 170 116 C110 122 45 135 12 160 Z" fill="var(--white)"/>
      <rect x="137" y="22" width="52" height="9" rx="4.5" fill="var(--white)"/>
      <circle cx="163" cy="22" r="5" fill="var(--white)"/>
    </svg>
    <div class="brand-name">JesterVolt</div>
    <div class="tagline">High-Quality<br>Latex Balloons</div>

    <div class="copy">
      <p>LOREM IPSUM IS SIMPLY DUMMY TEXT OF THE PRINTING AND TYPESETTING INDUSTRY. LOREM IPSUM HAS BEEN THE INDUSTRY'S STANDARD DUMMY TEXT EVER SINCE THE 1500S, WHEN AN UNKNOWN PRINTER TOOK A GALLEY OF TYPE AND SCRAMBLED IT TO MAKE A TYPE SPECIMEN BOOK.</p>
      <p>IT HAS SURVIVED NOT ONLY FIVE CENTURIES, BUT ALSO THE LEAP INTO ELECTRONIC TYPESETTING, REMAINING ESSENTIALLY UNCHANGED. IT WAS POPULARISED IN THE 1960S WITH THE RELEASE OF LETRASET SHEETS CONTAINING LOREM IPSUM PASSAGES, AND MORE RECENTLY WITH DESKTOP PUBLISHING SOFTWARE LIKE ALDUS PAGEMAKER INCLUDING VERSIONS OF LOREM IPSUM</p>
      <p>CONTRARY TO POPULAR BELIEF, LOREM IPSUM IS NOT SIMPLY RANDOM TEXT. IT HAS ROOTS IN A PIECE OF CLASSICAL LATIN LITERATURE FROM 45 BC, MAKING IT OVER 2000 YEARS OLD.</p>
    </div>

    <div class="site">WWW.JESTERVOLTFUN.COM</div>
    <div class="shop-name">Jester Fun<br>Shop</div>
    <div class="shop-slogan">YOUR ONE STOP CLOWN SHOP!</div>
    <div class="shop-city">MILLBROOK FALLS, VERMONT</div>

    <div class="marks">
      <svg class="mark" viewBox="0 0 26 26" role="img" aria-label="Disposal symbol"><rect x="5" y="6" width="16" height="16" rx="2" fill="var(--ink)"/></svg>
      <svg class="mark" viewBox="0 0 26 26" role="img" aria-label="Not for ages 0 to 3 symbol"><circle cx="13" cy="13" r="11" fill="none" stroke="var(--red)" stroke-width="3"/><line x1="5" y1="5" x2="21" y2="21" stroke="var(--red)" stroke-width="3"/></svg>
      <svg class="mark" viewBox="0 0 26 26" role="img" aria-label="Recycling symbol"><circle cx="13" cy="13" r="10" fill="var(--ink)"/></svg>
      <svg class="mark" viewBox="0 0 26 26" role="img" aria-label="Conformity mark"><rect x="3" y="5" width="20" height="16" fill="var(--ink)"/></svg>
    </div>

    <div class="specs">
      <div class="specs__big">MADE OF 100%</div>
      <div class="specs__mid">NATURAL RUBBER LATEX</div>
      <div class="specs__small">WHICH MAY CAUSE ALLERGIC REACTIONS</div>
      <div class="specs__foot">NET WT 25G &nbsp;MADE IN CHINA</div>
    </div>
  </section>

</div>
</body>
</html>
```